CD Cover (2 Sided Front & Single Sided Back) for Velmira Band

We compose electronic music with elements from the 80s and the 90s and we are ready to release our first album. We need a simple and elegant design for our covers that matches our music. You can listen to most of the tracks here: http://tunecastle.example/velmira . We have an existing logo that we would like to use. You can find the tracklist and the logo in the attachments. The title of the album is "Velmira - LP".

Industry/Entity Type

Electronic

```html
<!DOCTYPE html>
<html lang="en">
<head>
<meta charset="utf-8">
<title>Velmira - LP · CD Cover</title>
<link rel="stylesheet" href="https://fonts.googleapis.com/css2?family=Jura:wght@300;400;500&display=swap">
<style>
  :root {
    --ink-dark: #0e0a16;
    --glow: #fff8e6;
    --teal: #2b8c8a;
    --track-ink: #3a2a52;
    --white: #ffffff;
  }
  * { margin: 0; padding: 0; box-sizing: border-box; }
  html, body { width: 1200px; height: 597px; overflow: hidden; background: var(--ink-dark); }
  .cover {
    position: relative;
    width: 1200px;
    height: 597px;
    display: flex;
    font-family: "Jura", sans-serif;
    font-weight: 400;
  }
  .panel { position: relative; width: 600px; height: 597px; overflow: hidden; }

  .back-photo {
    position: absolute; inset: 0;
    background:
      radial-gradient(ellipse 260px 200px at 470px 250px, var(--glow) 0%, rgba(255,240,210,0.85) 35%, rgba(243,199,154,0) 80%),
      radial-gradient(ellipse 200px 110px at 150px 330px, rgba(180,87,138,0.75) 0%, rgba(58,31,69,0.6) 55%, rgba(58,31,69,0) 100%),
      linear-gradient(180deg, #d8b49a 0%, #f0c9a0 30%, #f6dcb8 55%, #6e4a5c 78%, #1c1422 88%, var(--ink-dark) 100%);
  }
  .front-photo {
    position: absolute; inset: 0;
    background:
      radial-gradient(ellipse 190px 110px at 110px 260px, rgba(127,199,184,0.85) 0%, rgba(60,110,120,0.5) 50%, rgba(60,110,120,0) 100%),
      radial-gradient(ellipse 260px 120px at 330px 210px, rgba(180,87,138,0.55) 0%, rgba(58,31,69,0.35) 60%, rgba(58,31,69,0) 100%),
      radial-gradient(ellipse 220px 160px at 560px 210px, rgba(246,216,180,0.95) 0%, rgba(243,199,154,0) 80%),
      linear-gradient(180deg, #6c5a6a 0%, #c9a08e 18%, #8a6a7c 40%, #4a3358 60%, #1a1224 78%, var(--ink-dark) 100%);
  }

  .album-mark {
    position: absolute;
    display: flex;
    align-items: baseline;
    line-height: 1;
    white-space: nowrap;
  }
  .album-mark .name { font-weight: 500; }

  .back .album-mark { top: 14px; right: 13px; gap: 4px; }
  .back .album-mark .name { font-size: 27px; color: var(--track-ink); }
  .back .album-mark .edition { font-size: 17px; color: var(--white); font-weight: 300; }

  .tracklist {
    position: absolute;
    top: 52px;
    right: 15px;
    list-style: none;
    text-align: right;
  }
  .track {
    display: block;
    height: 22.9px;
    font-size: 21px;
    line-height: 22.9px;
    color: var(--track-ink);
    white-space: nowrap;
  }
  .track .time {
    display: inline-block;
    width: 24px;
    margin-left: 4px;
    font-size: 12px;
    text-align: left;
  }

  .front .album-mark { top: 484px; left: 174px; gap: 10px; }
  .front .album-mark .name { font-size: 54px; color: var(--teal); letter-spacing: 1px; }
  .front .album-mark .edition { font-size: 21px; color: var(--white); font-weight: 300; align-self: flex-start; margin-top: 14px; }
</style>
</head>
<body>
  <main class="cover">
    <section class="panel back">
      <div class="back-photo" role="img" aria-label="Close-up photograph of dark fine netting curled against a warm peach and white glowing light"></div>
      <div class="album-mark">
        <span class="name">Velmira</span><span class="edition">LP</span>
      </div>
      <ol class="tracklist">
        <li class="track">1. Lantern<span class="time">3:05</span></li>
        <li class="track">2. 5th Tide<span class="time">4:18</span></li>
        <li class="track">3. 6th Tide<span class="time">3:57</span></li>
        <li class="track">4. 3rd Tide<span class="time">4:33</span></li>
        <li class="track">5. Afterglow<span class="time">3:41</span></li>
        <li class="track">6. Echoland<span class="time">3:22</span></li>
        <li class="track">7. 2nd Tide<span class="time">3:08</span></li>
        <li class="track">8. 1st Tide<span class="time">6:17</span></li>
        <li class="track">9. 4th Tide<span class="time">3:52</span></li>
        <li class="track">10. Nearer to you<span class="time">3:27</span></li>
      </ol>
    </section>
    <section class="panel front">
      <div class="front-photo" role="img" aria-label="Photograph of flowing translucent netting in teal, magenta and violet tones against a warm sky fading to dark"></div>
      <div class="album-mark">
        <span class="name">Velmira</span><span class="edition">LP</span>
      </div>
    </section>
  </main>
</body>
</html>
```